Powerpoint master slide deck for power point presentation by members of my company

To design a master slide deck for powerpoint presentation for a Orthopaedic Clinic Based in Singapore

```html
<!DOCTYPE html>
<html lang="en">
<head>
<meta charset="utf-8">
<title>Stride Joint Clinic – Master Slide Deck</title>
<link href="https://fonts.googleapis.com/css2?family=Exo+2:wght@600;700;800&family=Poppins:wght@400;500;600&display=swap" rel="stylesheet">
<style>
:root{
  --canvas:#1f1f1f;
  --teal:#4fb0a6;
  --teal-dark:#2f8c83;
  --teal-soft:#cfe9e5;
  --ink:#1d2727;
  --muted:#4a5555;
  --paper:#ffffff;
  --mist:#eef3f2;
}
*{box-sizing:border-box;margin:0;padding:0}
html,body{width:1200px;height:3888px;overflow:hidden;background:var(--canvas)}
body{position:relative;font-family:"Poppins",sans-serif;color:var(--ink)}
.slide{position:absolute;left:80px;width:1040px;height:585px;background:var(--paper);overflow:hidden}
.abs{position:absolute}
h1,h2,.brand-name{font-family:"Exo 2",sans-serif}
.heading{position:absolute;left:44px;top:28px;font-size:38px;font-weight:800;color:var(--ink)}
.heading span{color:var(--teal)}
.photo{position:absolute;background:linear-gradient(135deg,#a9c7c3,#6e8f8b)}
.brand{position:absolute;display:flex;align-items:center;gap:10px}
.brand-mark{width:26px;height:26px;background:var(--teal);border-radius:4px}
.brand-name{font-size:22px;font-weight:700;color:var(--teal-dark);line-height:1}
.body-text{font-size:13.5px;line-height:1.65;color:var(--muted)}
.socials{position:absolute;display:flex;gap:12px}
.socials i{width:30px;height:30px;border-radius:50%;background:var(--paper);display:block}
.wave{position:absolute;left:0;bottom:0}

/* slide 1 */
.s-welcome{top:48px;background:linear-gradient(120deg,#8fb3ae,#5f9c95)}
.s-welcome .band{position:absolute;inset:0}
.s-welcome .pill{left:500px;top:150px;background:var(--paper);color:var(--teal-dark);font-size:13px;font-weight:500;padding:7px 22px;border-radius:20px}
.s-welcome h1{left:500px;top:192px;font-size:58px;line-height:1.05;color:var(--paper);font-weight:800;width:500px}
.s-welcome .lede{left:500px;top:332px;width:440px;color:var(--paper);font-size:15px;line-height:1.5}

/* slide 2 */
.s-why{top:688px}
.s-why .intro{left:44px;top:92px;width:540px}
.s-why .plans-title{left:44px;top:338px;font-weight:600;font-size:16px}
.badges{position:absolute;left:44px;top:372px;display:grid;grid-template-columns:repeat(4,96px);gap:14px 22px}
.badges i{display:block;height:44px;border-radius:6px;background:var(--mist);border:1px solid #dde6e4}

/* slide 3 */
.s-services{top:1328px}
.grid{position:absolute;left:44px;top:100px;display:grid;grid-template-columns:repeat(4,220px);gap:18px 24px}
.tile{position:relative;height:170px}
.tile .photo{inset:0}
.tile .label{position:absolute;left:0;right:0;bottom:10px;margin:0 12px;background:var(--paper);border-radius:4px;font-size:13px;font-weight:600;padding:5px 10px;text-align:center}

/* slide 4 */
.s-fund{top:1968px}
.s-fund .para{left:44px;width:950px}
.features{position:absolute;left:120px;top:340px;display:flex;gap:130px}
.feature{width:200px;text-align:center}
.feature .box{width:110px;height:110px;border-radius:14px;background:var(--teal);margin:0 auto 14px;display:flex;align-items:center;justify-content:center}
.feature p{font-size:16px;font-weight:500}

/* slide 5 */
.s-team{top:2608px}
.doc{position:absolute;top:110px;width:300px}
.doc .photo{position:relative;height:200px;width:190px}
.doc h2{font-size:20px;color:var(--teal-dark);margin-top:14px}
.doc .role{font-size:12px;color:var(--teal);font-weight:500;margin-bottom:8px}
.doc .bio{font-size:12.5px;line-height:1.6;color:var(--muted)}
.centre-mark{position:absolute;left:430px;top:150px;width:180px;height:180px;border-radius:24px;background:var(--teal);display:flex;align-items:center;justify-content:center;text-align:center;color:var(--paper);font-family:"Exo 2",sans-serif;font-weight:700;font-size:24px;line-height:1.1}

/* slide 6 */
.s-contact{top:3248px;background:linear-gradient(120deg,#5fa9a1,#2f8c83);color:var(--paper)}
.s-contact h2{position:absolute;left:44px;top:30px;font-size:30px;font-weight:700}
.contact-list{position:absolute;left:44px;top:90px;display:flex;flex-direction:column;gap:22px;width:470px}
.contact-item{display:flex;gap:14px}
.contact-item svg{flex:none}
.contact-item b{display:block;font-size:16px;font-weight:600}
.contact-item span{font-size:13px;opacity:.9}
.s-contact .thanks{left:44px;top:382px;font-family:"Exo 2",sans-serif;font-size:64px;font-weight:800}
.s-contact .brand{left:44px;top:478px}
.s-contact .brand-mark{background:var(--paper)}
.s-contact .brand-name{color:var(--paper);font-size:28px}
</style>
</head>
<body>

<!-- Slide 1: Welcome -->
<section class="slide s-welcome">
  <svg class="band" width="1040" height="585" viewBox="0 0 1040 585">
    <polygon points="0,0 420,0 300,585 0,585" fill="#3f9d94" opacity=".35"/>
    <polygon points="760,585 1040,300 1040,585" fill="#2f8c83" opacity=".5"/>
  </svg>
  <div class="photo" role="img" aria-label="Surgeon examining a patient's knee" style="left:80px;top:70px;width:340px;height:440px;border-radius:6px"></div>
  <div class="abs pill">Double Fellowship Trained Orthopaedic Surgeons</div>
  <h1 class="abs">Welcome To Stride Joint Clinic</h1>
  <p class="abs lede">Our mission is to promote individualised care that meets the needs and goals of every patient.</p>
  <div class="socials" style="left:500px;top:410px"><i></i><i></i><i></i><i></i></div>
</section>

<!-- Slide 2: Why Choose Us -->
<section class="slide s-why">
  <h2 class="heading">Why <span>Choose Us?</span></h2>
  <div class="abs intro body-text">
    <p>We take pride in our patient centred and honest approach, offering services that are sustainable and affordable for our clients.</p><br>
    <p>Both our doctors are MedFund-accredited, and patients may use their MedFund for eligible procedures, consultations, and medications. We strongly believe that non-surgical treatments should always be the first option, with surgery explored only if needed. Our clinic is on the panel of most Integrated Shield Plans, Singapore.</p>
  </div>
  <p class="abs plans-title">MedFund &amp; Integrated Shield Plans Approved</p>
  <div class="badges"><i></i><i></i><i></i><i></i><i></i><i></i></div>
  <div class="abs" style="left:640px;top:84px;width:340px;height:330px;background:var(--teal)"></div>
  <div class="photo" role="img" aria-label="Portrait of the clinic's two surgeons" style="left:620px;top:64px;width:340px;height:330px;background:linear-gradient(135deg,#eef1f0,#c9d3d1)"></div>
  <svg class="wave" width="400" height="90" viewBox="0 0 400 90"><path d="M0 40 Q160 90 400 60 L400 90 L0 90Z" fill="var(--teal)"/></svg>
  <div class="brand" style="right:40px;bottom:28px"><i class="brand-mark"></i><span class="brand-name">Stride Joint Clinic</span></div>
</section>

<!-- Slide 3: What We Do -->
<section class="slide s-services">
  <h2 class="heading">What <span>We Do</span></h2>
  <div class="grid">
    <div class="tile"><div class="photo" role="img" aria-label="Knee evaluation"></div><div class="label">Knee Evaluation</div></div>
    <div class="tile"><div class="photo" role="img" aria-label="Meniscus repair"></div><div class="label">Meniscus Repair</div></div>
    <div class="tile"><div class="photo" role="img" aria-label="ACL reconstruction"></div><div class="label">ACL Tear &amp; Reconstruction</div></div>
    <div class="tile"><div class="photo" role="img" aria-label="Hip replacement"></div><div class="label">Hip Replacement</div></div>
    <div class="tile"><div class="photo" role="img" aria-label="Hip evaluation"></div><div class="label">Hip Evaluation</div></div>
    <div class="tile"><div class="photo" role="img" aria-label="Cartilage repair"></div><div class="label">Cartilage Repair</div></div>
    <div class="tile"><div class="photo" role="img" aria-label="Knee replacement implants"></div><div class="label">Knee Replacement</div></div>
    <div class="tile"><div class="photo" role="img" aria-label="Bone wellness"></div><div class="label">Bone Wellness</div></div>
  </div>
  <div class="brand" style="right:40px;bottom:18px"><i class="brand-mark"></i><span class="brand-name">Stride Joint Clinic</span></div>
</section>

<!-- Slide 4: Accreditation -->
<section class="slide s-fund">
  <h2 class="heading">We are <span>MedFund-accredited</span></h2>
  <p class="abs para body-text" style="top:96px">We believe that all our patients deserve efficient care for their musculoskeletal conditions. We are passionate about seeing patients regain their independence in mobility, improve their quality of life and enjoy precious time with their loved ones.</p>
  <p class="abs para body-text" style="top:196px">Our mission is to provide personalised care that accommodates every patient's needs and goals. We pride ourselves on offering services that are sustainable and affordable for our clients. Both doctors are MedFund accredited, and patients may use their MedFund for eligible procedures, consultations, and medications.</p>
  <div class="features">
    <div class="feature"><div class="box"><svg width="54" height="54" viewBox="0 0 54 54" fill="none" stroke="#fff" stroke-width="3"><rect x="8" y="14" width="38" height="28" rx="4"/><circle cx="27" cy="28" r="7"/></svg></div><p>MedFund</p></div>
    <div class="feature"><div class="box"><svg width="54" height="54" viewBox="0 0 54 54" fill="none" stroke="#fff" stroke-width="3"><path d="M27 6 L44 13 V27 C44 38 36 45 27 48 C18 45 10 38 10 27 V13Z"/><path d="M27 19v16M19 27h16"/></svg></div><p>Integrated Shield Plans</p></div>
    <div class="feature"><div class="box"><svg width="54" height="54" viewBox="0 0 54 54" fill="none" stroke="#fff" stroke-width="3"><path d="M14 6h20l8 8v34H14Z"/><path d="M20 30l6 6 10-12"/></svg></div><p>Corporate Insurance</p></div>
  </div>
  <div class="brand" style="right:40px;bottom:22px"><i class="brand-mark"></i><span class="brand-name">Stride Joint Clinic</span></div>
</section>

<!-- Slide 5: Team -->
<section class="slide s-team">
  <h2 class="heading">What <span>We Do</span></h2>
  <div class="doc" style="left:100px">
    <div class="photo" role="img" aria-label="Portrait of Dr Marcus Teo"></div>
    <h2>Dr Marcus Teo</h2>
    <p class="role">Orthopaedic Surgery Specialist</p>
    <p class="bio">Dr Marcus Teo is an orthopaedic surgeon with subspeciality training in primary and complex hip and knee replacements.</p>
  </div>
  <div class="centre-mark">Stride<br>Joint<br>Clinic</div>
  <div class="doc" style="left:690px">
    <div class="photo" role="img" aria-label="Portrait of Dr Lim Wei Ling"></div>
    <h2>Dr Lim Wei Ling</h2>
    <p class="role">Orthopaedic Surgery Specialist</p>
    <p class="bio">Dr Lim is an orthopaedic surgeon with subspeciality training in hip and knee surgery, leading our joint care team.</p>
  </div>
  <div class="brand" style="right:40px;bottom:22px"><i class="brand-mark"></i><span class="brand-name">Stride Joint Clinic</span></div>
</section>

<!-- Slide 6: Contact -->
<section class="slide s-contact">
  <h2>Get In Touch With Us</h2>
  <div class="contact-list">
    <div class="contact-item">
      <svg width="28" height="28" viewBox="0 0 24 24" fill="#fff"><path d="M12 2a7 7 0 0 0-7 7c0 5 7 13 7 13s7-8 7-13a7 7 0 0 0-7-7zm0 9.5A2.5 2.5 0 1 1 12 6.5a2.5 2.5 0 0 1 0 5z"/></svg>
      <div><b>Address:</b><span>Northvale Specialist Centre, 12 Kestrel Road, #05-14 Singapore 300512</span></div>
    </div>
    <div class="contact-item">
      <svg width="28" height="28" viewBox="0 0 24 24" fill="none" stroke="#fff" stroke-width="2"><rect x="3" y="5" width="18" height="14" rx="2"/><path d="M3 7l9 6 9-6"/></svg>
      <div><b>Email Us:</b><span>hello@stridejoint.sg</span></div>
    </div>
    <div class="contact-item">
      <svg width="28" height="28" viewBox="0 0 24 24" fill="#fff"><path d="M6.6 10.8a15 15 0 0 0 6.6 6.6l2.2-2.2a1 1 0 0 1 1-.25 11.4 11.4 0 0 0 3.6.6 1 1 0 0 1 1 1V20a1 1 0 0 1-1 1A17 17 0 0 1 3 4a1 1 0 0 1 1-1h3.5a1 1 0 0 1 1 1c0 1.25.2 2.45.6 3.6a1 1 0 0 1-.25 1z"/></svg>
      <div><b>Phone Number:</b><span>+65 6000 1234</span></div>
    </div>
  </div>
  <p class="abs thanks">Thank You</p>
  <div class="brand"><i class="brand-mark"></i><span class="brand-name">Stride Joint Clinic</span></div>
  <div class="photo" role="img" aria-label="Doctor reassuring a smiling patient" style="left:560px;top:60px;width:440px;height:400px;border-radius:10px;background:linear-gradient(135deg,#d9e4e2,#9fbab6)"></div>
  <div class="socials" style="left:700px;top:490px"><i></i><i></i><i></i><i></i></div>
</section>

</body>
</html>
```